Freeze dried pet treats and chews packaging design

We are an Belgium based brand selling all natural treats and chews for pets. We are looking for a full color packaging design for a new line of freeze dried treats and chews for cats and dogs. The design should look familiar for our customers with our existing logo, but with a fresh new design especially for this new line. It should reflect our core values of natural, species appropriate food products without any additives or nasties.
The packaging will be a stand-up pouch with zipper, eurohole, easy open and with a window somewhere in the design to show the products inside. Please present your design as a mockup if possible.
Name of the product will be "Velmo Freeze Dried Bitzoos". Add icons to emphasize certain aspects of the product:
- 100% natural
- freeze dried (preserves all nutrients best)
- 100% mono protein
- without additives
- high in protein
- high in flavor
The design is a generic one for 12 different products, only one pouch will be produced and finished with 12 different round labels to indicate the protein source (beef, chicken, lamb, etc). You can include one of these stickers on your design to make the example complete. The sticker should have a separate color for every protein source to make it good distinguishable, an icon representing the protein source (see examples of existing packaging) and a round text around it with the protein source in text in Dutch, French and English (example: RUND - BŒUF - BEEF).
Important: after this design we need more designs for other new product lines, so the winner might get more out of this then only this one project!
High premium pet products
Petfood
- Fontastique, Roboto (used for logo and current designs), others welcome too

```html
<!DOCTYPE html>
<html lang="en">
<head>
<meta charset="utf-8">
<title>Velmo Freeze Dried Bitzoos – Pouch Front</title>
<link rel="stylesheet" href="https://fonts.googleapis.com/css2?family=Fredoka:wght@400;500;600&display=swap">
<style>
  :root {
    --stage: #3bb8e5;
    --cream: #f2f5e6;
    --cream-shade: #e4e9d2;
    --lime: #9cc63d;
    --lime-soft: #d9e8b0;
    --purple: #4d1a8c;
    --purple-deep: #35106b;
    --purple-light: #9c73c4;
    --blue: #1f93e2;
    --beef: #6b2418;
    --beef-light: #f4ead9;
    --white: #ffffff;
  }
  * { margin: 0; padding: 0; box-sizing: border-box; }
  html, body { width: 1023px; height: 1200px; overflow: hidden; }
  body {
    background: var(--stage);
    font-family: "Fredoka", sans-serif;
    display: flex;
    align-items: center;
    justify-content: center;
  }
  .pouch { width: 711px; height: 1100px; display: block; }
  .brand-name { font-family: "Fredoka", sans-serif; font-weight: 600; fill: var(--purple); }
  .line-name { font-family: "Fredoka", sans-serif; font-weight: 600; }
  .line-name--top { fill: var(--blue); }
  .line-name--bottom { fill: var(--purple); }
  .claim-label { font-family: "Fredoka", sans-serif; font-weight: 500; font-size: 21px; fill: var(--purple); }
  .claim-label--dark { fill: var(--purple-deep); }
  .sticker-text { font-family: "Fredoka", sans-serif; font-weight: 600; font-size: 15px; fill: var(--beef); letter-spacing: 1px; }
  .weight-text { font-family: "Fredoka", sans-serif; font-size: 19px; fill: var(--purple-deep); }
  .seal-caption { font-family: "Fredoka", sans-serif; font-size: 15px; fill: var(--white); }
  .footer-title { font-family: "Fredoka", sans-serif; font-weight: 500; font-size: 22px; fill: var(--white); }
  .footer-line { font-family: "Fredoka", sans-serif; font-size: 19px; fill: var(--white); }
</style>
</head>
<body>
<svg class="pouch" viewBox="0 0 882 1365" xmlns="http://www.w3.org/2000/svg" aria-label="Velmo Freeze Dried Bitzoos stand-up pouch, front">
  <defs>
    <linearGradient id="purple-band" x1="0" y1="0" x2="1" y2="0">
      <stop offset="0" stop-color="#2f0c63"/>
      <stop offset="0.55" stop-color="#5a2596"/>
      <stop offset="1" stop-color="#a27ccb"/>
    </linearGradient>
    <radialGradient id="treats" cx="0.55" cy="0.45" r="0.7">
      <stop offset="0" stop-color="#f2d9a4"/>
      <stop offset="0.6" stop-color="#e0a860"/>
      <stop offset="1" stop-color="#b5703a"/>
    </radialGradient>
    <linearGradient id="cream-body" x1="0" y1="0" x2="1" y2="0">
      <stop offset="0" stop-color="#e6ead6"/>
      <stop offset="0.12" stop-color="#f2f5e6"/>
      <stop offset="0.9" stop-color="#f4f7ea"/>
      <stop offset="1" stop-color="#e3e8d1"/>
    </linearGradient>
    <clipPath id="pouch-shape">
      <path d="M20 0 H862 Q882 0 882 22 V1365 H0 V22 Q0 0 20 0 Z"/>
    </clipPath>
    <path id="arc-sticker-top" d="M90 305 A50 50 0 1 1 184 305"/>
    <path id="arc-sticker-bottom" d="M89 316 A56 56 0 0 0 185 316"/>
    <path id="arc-mono" d="M245 833 A66 66 0 0 1 354 763"/>
    <path id="arc-additives" d="M362 721 A80 80 0 0 1 512 721"/>
    <path id="arc-protein" d="M528 708 A74 74 0 0 1 656 708"/>
    <path id="arc-flavor" d="M657 766 A66 66 0 0 1 755 834"/>
  </defs>

  <g clip-path="url(#pouch-shape)">
    <rect class="pouch-body" width="882" height="1365" fill="url(#cream-body)"/>
    <rect class="top-stripe" x="56" y="0" width="154" height="215" fill="var(--lime)"/>
    <rect class="zipper" x="0" y="145" width="882" height="8" fill="var(--cream-shade)"/>
    <rect class="zipper" x="0" y="160" width="882" height="4" fill="var(--cream-shade)"/>

    <path class="wave-soft" d="M0 780 C200 740 420 790 600 760 C720 740 820 700 882 640 V960 H0 Z" fill="var(--lime-soft)"/>
    <path class="wave-lime" d="M0 895 C180 860 300 880 420 860 C600 830 760 790 882 700 V990 H0 Z" fill="var(--lime)"/>
    <path class="wave-cream" d="M0 915 C190 885 320 905 440 885 C610 855 770 810 882 735 V1000 H0 Z" fill="var(--cream)"/>
    <path class="wave-lime-thin" d="M560 1010 C680 960 790 900 882 810 V860 C790 940 690 1000 600 1040 Z" fill="var(--lime-soft)"/>

    <path class="purple-band" d="M0 905 C170 880 300 905 420 930 C600 970 760 960 882 890 V1365 H0 Z" fill="url(#purple-band)"/>

    <path class="window-frame" d="M110 1060 C150 1000 260 960 330 900 C390 840 440 820 520 822 C640 826 705 920 705 1040 C705 1180 610 1260 470 1262 C330 1264 250 1160 150 1100 C120 1085 100 1075 110 1060 Z" fill="var(--lime)"/>
    <path class="window" role="img" aria-label="Clear window showing the freeze dried beef chunks inside" d="M140 1062 C180 1015 280 985 345 925 C400 870 445 855 520 857 C620 860 675 940 675 1040 C675 1160 595 1230 470 1232 C345 1234 265 1140 175 1090 C150 1080 132 1072 140 1062 Z" fill="url(#treats)"/>

    <line x1="172" y1="1292" x2="322" y2="1290" stroke="var(--lime)" stroke-width="2"/>
    <line x1="568" y1="1289" x2="720" y2="1285" stroke="var(--lime)" stroke-width="2"/>
    <text class="footer-title" x="444" y="1298" text-anchor="middle">Premium Pet Products</text>
    <text class="footer-line" x="444" y="1328" text-anchor="middle">Natural, Species Appropriate Food Products without any</text>
    <text class="footer-line" x="444" y="1354" text-anchor="middle">Additives or Nasties.</text>
  </g>

  <g class="protein-sticker">
    <circle cx="137" cy="288" r="74" fill="var(--beef)"/>
    <circle cx="137" cy="288" r="65" fill="var(--beef-light)"/>
    <circle cx="137" cy="288" r="44" fill="none" stroke="var(--beef)" stroke-width="1.5"/>
    <circle cx="137" cy="288" r="26" fill="var(--beef)" role="img" aria-label="Cow icon marking the beef protein source"/>
    <text class="sticker-text"><textPath href="#arc-sticker-top" startOffset="50%" text-anchor="middle">RUND - BŒUF - BEEF</textPath></text>
    <text class="sticker-text"><textPath href="#arc-sticker-bottom" startOffset="50%" text-anchor="middle">FLAVOR</textPath></text>
  </g>

  <g class="brand">
    <circle cx="330" cy="312" r="12" fill="var(--lime)"/>
    <text class="brand-name" x="452" y="335" font-size="78" text-anchor="middle">Velmo</text>
  </g>

  <g class="snowflake" stroke="var(--blue)" stroke-width="3" stroke-linecap="round">
    <line x1="137" y1="442" x2="137" y2="498"/><line x1="113" y1="456" x2="161" y2="484"/><line x1="113" y1="484" x2="161" y2="456"/>
  </g>
  <g class="snowflake" stroke="var(--blue)" stroke-width="3" stroke-linecap="round">
    <line x1="740" y1="442" x2="740" y2="498"/><line x1="716" y1="456" x2="764" y2="484"/><line x1="716" y1="484" x2="764" y2="456"/>
  </g>
  <text class="line-name line-name--top" x="438" y="500" font-size="96" text-anchor="middle">Freeze Dried</text>
  <text class="line-name line-name--bottom" x="448" y="598" font-size="92" text-anchor="middle">Bitzoos</text>

  <g class="claim">
    <circle cx="307" cy="810" r="52" fill="var(--purple)"/>
    <circle cx="307" cy="810" r="40" fill="none" stroke="var(--white)" stroke-width="2"/>
    <g stroke="var(--white)" stroke-width="2.5" stroke-linecap="round">
      <line x1="290" y1="828" x2="310" y2="792"/><line x1="298" y1="830" x2="318" y2="794"/><line x1="306" y1="830" x2="326" y2="794"/>
    </g>
    <text class="claim-label claim-label--dark"><textPath href="#arc-mono" startOffset="50%" text-anchor="middle">100% Mono Protein</textPath></text>
  </g>
  <g class="claim">
    <ellipse cx="437" cy="748" rx="52" ry="62" fill="var(--purple)"/>
    <circle cx="437" cy="748" r="38" fill="none" stroke="var(--white)" stroke-width="2.5"/>
    <line x1="410" y1="721" x2="464" y2="775" stroke="var(--white)" stroke-width="2.5"/>
    <text class="claim-label claim-label--dark"><textPath href="#arc-additives" startOffset="50%" text-anchor="middle">Without Additives</textPath></text>
  </g>
  <g class="claim">
    <ellipse cx="592" cy="745" rx="55" ry="60" fill="var(--purple-light)"/>
    <circle cx="592" cy="745" r="40" fill="none" stroke="var(--white)" stroke-width="2"/>
    <rect x="575" y="722" width="34" height="44" rx="5" fill="none" stroke="var(--white)" stroke-width="2"/>
    <text class="claim-label"><textPath href="#arc-protein" startOffset="50%" text-anchor="middle">High in Protein</textPath></text>
  </g>
  <g class="claim">
    <ellipse cx="690" cy="823" rx="47" ry="52" fill="var(--purple-light)"/>
    <circle cx="690" cy="823" r="34" fill="none" stroke="var(--white)" stroke-width="2"/>
    <text class="claim-label"><textPath href="#arc-flavor" startOffset="50%" text-anchor="middle">High in Flavor</textPath></text>
  </g>

  <path class="weight-blob" d="M135 1138 C170 1138 182 1165 182 1190 C182 1218 160 1228 135 1228 C105 1228 90 1210 90 1185 C90 1160 105 1138 135 1138 Z" fill="var(--lime)"/>
  <text class="weight-text" x="136" y="1190" text-anchor="middle">200 gm</text>

  <g class="seal" role="img" aria-label="100% natural seal">
    <circle cx="742" cy="1050" r="32" fill="none" stroke="var(--white)" stroke-width="2.5"/>
    <circle cx="742" cy="1050" r="22" fill="none" stroke="var(--white)" stroke-width="1.5"/>
  </g>
  <g class="seal" role="img" aria-label="Freeze dried seal">
    <circle cx="742" cy="1140" r="32" fill="none" stroke="var(--white)" stroke-width="2.5"/>
    <circle cx="742" cy="1140" r="22" fill="none" stroke="var(--white)" stroke-width="1.5"/>
  </g>
  <text class="seal-caption" x="740" y="1196" text-anchor="middle">Preserves</text>
  <text class="seal-caption" x="740" y="1214" text-anchor="middle">All Nutrients Best</text>
</svg>
</body>
</html>
```